The cardstock I will be printing on measures 3 1/2” x 2 3/8 “ the design will be a redesign of another logo and modified to fit the cardstock that will be added to a blister pack for packaging. The background needs to be a light prism with multiple colors like the Lumo logo provided.
The name is Lumo Botanics
Please design label with same layout as photo take in AI except make the logo look like the Lumo logo with rainbow light background and Lumo Botanics added to the logo.
Please contact me for more details and photos if needed.

The logo I need made is the Lumo logo. The packaging will be just like the Dorimel packaging, so please use that as a reference to where the cartridge will sit in the packaging.
I will also need round and square labels made and I’m willing to pay for all designs.
Thank you for your assistance. The Lumo logo will no stretch due to not being a vectorized image and I don’t have means of creating it myself.

Target Market(s)

Medical Marijuana

Font styles to use
Sans Serif

Colors

Designer to choose colors to be used in the design.

Requirements
Must have
• The label must look like the Lumo label provided.
• The Lumo label provided is not a vectorized image and is just a phot so i can not stretch and modify it.
• Please recreate this logo to the best of your abilities and make it into a label resembling the rough draft provided to the best of your abilities.
• I will need a round logo with the same design for stickers and a square logo with the same design for stickers as well.
Nice to have
• As similar to the Lumo label provided as possible except making it into a label that will fit the provided measurements and work around where the cartridge will be positioned.
Should not have
• Anything different than the simplistic layout provided please. It needs to resemble it as much as possible except it needs to be crisp and clear.

```html
<!DOCTYPE html>
<html lang="en">
<head>
<meta charset="utf-8">
<title>Lumo Botanics – Cartridge Blister Card</title>
<link rel="stylesheet" href="https://fonts.googleapis.com/css2?family=Lato:wght@300;400;700;900&family=Cinzel:wght@500&display=swap">
<style>
  :root {
    --page-bg: #e4e4e4;
    --ink: #111111;
    --white: #ffffff;
    --badge-yellow: #f7e05a;
    --warn-red: #e3202b;
    --red: #f0163c;
    --yellow: #f3ef22;
    --magenta: #d9128f;
    --violet: #8c45c9;
    --cyan: #5fd3e6;
    --aqua: #18dff0;
    --sky: #2fa6ee;
    --green: #1ccf5a;
    --deep-green: #0c9a22;
    --lime: #c9ec3a;
  }
  * { margin: 0; padding: 0; box-sizing: border-box; }
  html, body { width: 1200px; height: 900px; overflow: hidden; }
  body {
    background: var(--page-bg);
    font-family: "Lato", sans-serif;
    color: var(--ink);
    position: relative;
  }
  .card {
    position: absolute;
    top: 170px;
    width: 344px;
    height: 506px;
    border-radius: 16px;
    overflow: hidden;
  }
  .card--front {
    left: 188px;
    background:
      radial-gradient(circle at 64% 30%, rgba(255,255,255,0.95) 0, rgba(255,255,255,0.55) 60px, rgba(255,255,255,0) 150px),
      radial-gradient(circle at 55% 80%, rgba(200,205,235,0.8) 0, rgba(200,205,235,0) 110px),
      radial-gradient(circle at 100% 100%, var(--cyan) 0, rgba(95,211,230,0) 170px),
      radial-gradient(circle at 0% 100%, var(--violet) 0, rgba(140,69,201,0) 180px),
      radial-gradient(circle at 100% 0%, var(--yellow) 0, rgba(243,239,34,0) 260px),
      linear-gradient(170deg, var(--red) 0%, #ec1f6a 40%, var(--magenta) 75%, #a6179d 100%);
  }
  .card--back {
    left: 668px;
    background:
      radial-gradient(circle at 50% 28%, rgba(255,255,255,0.95) 0, rgba(255,255,255,0.55) 55px, rgba(255,255,255,0) 140px),
      radial-gradient(circle at 0% 100%, var(--lime) 0, rgba(201,236,58,0) 200px),
      radial-gradient(circle at 100% 100%, var(--deep-green) 0, rgba(12,154,34,0) 220px),
      radial-gradient(circle at 0% 30%, var(--sky) 0, rgba(47,166,238,0) 180px),
      linear-gradient(135deg, var(--aqua) 0%, #3fe0c0 45%, var(--green) 75%, var(--deep-green) 100%);
  }

  .strain-badge {
    position: absolute;
    left: 33px; top: 23px;
    width: 86px; height: 86px;
    border-radius: 50%;
    background: var(--badge-yellow);
    display: flex; flex-direction: column; align-items: center; justify-content: center;
    font-family: "Cinzel", serif;
    font-weight: 500;
    font-size: 18px;
    line-height: 1.1;
    color: var(--ink);
  }
  .cartridge {
    position: absolute;
    left: 46px; top: 130px;
    width: 59px; height: 298px;
    border-radius: 22px 22px 6px 6px;
    background: linear-gradient(180deg, #ffffff 0%, #f1f1f1 45%, #c9c9cf 60%, #9ea0a8 80%, #d8d8dc 100%);
  }

  .brand-mark {
    position: absolute;
    display: flex; align-items: center; gap: 8px;
    font-weight: 700;
    font-size: 22px;
    color: var(--ink);
    white-space: nowrap;
  }
  .brand-mark__dot {
    width: 14px; height: 14px; border-radius: 50%;
    background: var(--ink);
  }
  .card--front .brand-mark { left: 222px; top: 116px; transform: translateX(-50%); }
  .card--back .brand-mark { left: 172px; top: 110px; transform: translateX(-50%); }

  .headline {
    position: absolute;
    text-align: center;
    font-weight: 700;
    font-size: 22.5px;
    line-height: 27px;
    white-space: nowrap;
  }
  .card--front .headline { left: 222px; top: 223px; transform: translateX(-50%); }
  .card--back .headline { left: 172px; top: 225px; transform: translateX(-50%); }

  .claim {
    position: absolute;
    left: 222px; top: 302px;
    transform: translateX(-50%);
    width: 200px;
    text-align: center;
    font-size: 13.5px;
    line-height: 17px;
  }
  .potency {
    position: absolute;
    left: 36px; top: 446px;
    font-weight: 300;
    font-size: 38px;
    color: var(--white);
    letter-spacing: -0.5px;
  }
  .warning-mark {
    position: absolute;
    left: 230px; top: 396px;
    width: 88px; height: 88px;
  }

  .story {
    position: absolute;
    left: 22px; top: 290px;
    width: 300px;
    text-align: center;
    font-size: 10px;
    line-height: 12px;
    letter-spacing: -0.3px;
  }
  .story p + p { margin-top: 12px; }
  .story strong { font-weight: 900; }

  .social {
    position: absolute;
    left: 172px; top: 430px;
    transform: translateX(-50%);
    display: flex; flex-direction: column; align-items: center; gap: 8px;
    font-size: 13.5px;
  }
  .social__dot {
    width: 26px; height: 26px; border-radius: 50%;
    background: var(--ink);
  }
</style>
</head>
<body>

  <section class="card card--front">
    <div class="strain-badge"><span>LEMON</span><span>HAZE</span></div>
    <div class="cartridge" role="img" aria-label="Photo of a white-tipped vape cartridge with metal base"></div>

    <div class="brand-mark"><span class="brand-mark__dot"></span>Lumo Botanics</div>

    <h1 class="headline">Premium Quality<br>Organic Cannabis oil</h1>
    <p class="claim">100% Natural Ingredients and absolutely no PG, VG, PEG or MCT Contains only pure cannabis oil and terpenes.</p>

    <div class="potency">90% THC</div>

    <svg class="warning-mark" viewBox="0 0 88 88" aria-hidden="true">
      <rect x="17" y="17" width="54" height="54" transform="rotate(45 44 44)" fill="#ffffff" stroke="#e3202b" stroke-width="6"/>
    </svg>
  </section>

  <section class="card card--back">
    <div class="brand-mark"><span class="brand-mark__dot"></span>Lumo Botanics</div>

    <h2 class="headline">Premium Quality<br>Organic Cannabis oil</h2>

    <div class="story">
      <p><strong>LUMO BOTANICS</strong> was a Lorem ipsum dolor sit amet, consectetur adipiscing elit, sed do eiusmod tempor incididunt ut labore et dolore magna aliqua.</p>
      <p>Ut enim ad minim veniam, quis nostrud exercitation ullamco laboris nisi ut aliquip ex ea commodo consequat.</p>
      <p>Duis aute irure dolor in reprehenderit in voluptate velit esse cillum dolore eu fugiat nulla pariatur. Excepteur sint occaecat cupidatat non proident, sunt in culpa qui officia deserunt mollit anim id est laborum.</p>
    </div>

    <div class="social">
      <span class="social__dot"></span>
      <span>@lumobotanics</span>
    </div>
  </section>

</body>
</html>
```